Therapist website

I need a sqaure space web design for my therapy practice. I need a home page, a services page with 4 subpages, an about me, an insurnace page, a contact page, an EMDR page

```html
<!DOCTYPE html>
<html lang="en">
<head>
<meta charset="utf-8">
<title>Brightmeadow Family Counseling</title>
<link href="https://fonts.googleapis.com/css2?family=Roboto:wght@300;400;500;700&display=swap" rel="stylesheet">
<style>
:root{
  --teal:#1c9aa6;
  --teal-bright:#0bc0c4;
  --teal-dark:#13808b;
  --ink:#1a1a1a;
  --muted:#333;
  --footer:#2a2a2a;
  --white:#fff;
}
*{box-sizing:border-box;margin:0;padding:0}
html,body{width:1200px;height:1200px;overflow:hidden;background:var(--white);font-family:"Roboto",Arial,sans-serif;color:var(--ink)}
.page{position:relative;width:1200px;height:1200px}
.abs{position:absolute}
.brand{left:371px;top:10px;font-size:10px;font-weight:500;color:var(--teal);letter-spacing:.5px;display:flex;align-items:center;gap:5px}
.brand-dot{width:9px;height:9px;border-radius:50%;background:var(--teal)}
.nav a{position:absolute;top:17px;font-size:6.5px;letter-spacing:2.4px;color:var(--ink);text-decoration:none}
.nav .active::after{content:"";position:absolute;left:0;right:2px;top:18px;height:2px;background:var(--teal-bright)}
.pill{display:flex;align-items:center;justify-content:center;border-radius:12px;font-size:5.6px;text-transform:uppercase;letter-spacing:.2px}
.pill-teal{background:var(--teal);color:var(--white);box-shadow:0 2px 3px rgba(0,0,0,.15)}
.pill-white{background:var(--white);color:var(--teal)}
.photo{border:0}
.hero-photo{left:375px;top:44px;width:447px;height:228px;background:linear-gradient(90deg,#e6dccb 0%,#d9c39a 45%,#c9a56a 75%,#b98e4f 100%)}
.hero-text{left:394px;top:114px;width:150px}
.eyebrow{font-size:6.5px;letter-spacing:2px}
.hero-title{font-size:16px;font-weight:400;margin-top:5px;letter-spacing:.2px}
.body-small{font-size:4.8px;line-height:7.8px;color:var(--muted)}
.band{background:linear-gradient(90deg,var(--teal) 0%,var(--teal-bright) 100%);display:flex;align-items:center}
.band-text{position:absolute;font-size:13px;font-weight:300;color:var(--white)}
.section-title{font-size:16px;font-weight:500;color:var(--teal-bright)}
.section-title span{color:var(--ink);font-weight:400}
.dot{display:inline-block;width:3px;height:3px;border-radius:50%;background:var(--teal-bright);margin-left:2px}
.services{left:375px;top:578px;width:447px;height:178px;background:var(--teal);color:var(--white)}
.services h2{position:absolute;top:23px;width:100%;text-align:center;font-size:15px;font-weight:300}
.services h2 b{font-weight:500}
.svc{position:absolute;top:64px;width:110px;text-align:center;transform:translateX(-50%)}
.svc svg{display:block;margin:0 auto 6px}
.svc h3{font-size:7.5px;font-weight:500}
.svc p{font-size:4.7px;line-height:8.5px;margin-top:5px;opacity:.9}
.svc a{display:block;font-size:5.5px;font-weight:700;color:var(--white);text-decoration:none;margin-top:7px}
.footer{left:376px;top:1062px;width:447px;height:113px;background:var(--footer);color:var(--white)}
.footer h4{position:absolute;top:22px;font-size:7.8px;font-weight:500}
.footer .col{position:absolute;top:44px;font-size:5.2px;line-height:9.2px;color:#ddd}
.contact-row{display:flex;align-items:center;gap:5px;height:12px}
.socials{display:flex;gap:4px;margin-top:4px}
.socials span{width:8px;height:8px;border-radius:50%;background:var(--teal-bright)}
.copy{left:0;width:1200px;top:1183px;text-align:center;font-size:5px;color:#444}
</style>
</head>
<body>
<div class="page">

  <div class="abs brand"><span class="brand-dot"></span>BRIGHTMEADOW</div>
  <nav class="nav">
    <a class="active" style="left:541px">HOME</a>
    <a style="left:586px">ABOUT ME</a>
    <a style="left:652px">INSURNACE</a>
    <a style="left:724px">EMDR</a>
  </nav>
  <div class="abs pill pill-teal" style="left:763px;top:13px;width:63px;height:17px">Contact Us</div>

  <div class="abs photo hero-photo" role="img" aria-label="Photo of a girl with raised arms in a golden wheat field"></div>
  <div class="abs hero-text">
    <div class="eyebrow">WELCOME TO</div>
    <div class="hero-title">BRIGHTMEADOW</div>
    <p class="body-small" style="margin-top:9px">Holisticly build progressive e-markets without long-term high-impact e-tailers. Intrinsicly e-enable cross-unit quality vectors without team building ROI.</p>
  </div>
  <div class="abs pill pill-teal" style="left:394px;top:184px;width:63px;height:17px">Contact Us</div>

  <div class="abs band" style="left:375px;top:272px;width:447px;height:42px">
    <span class="band-text" style="left:71px">Don't Wait to Get the Help You Need</span>
    <div class="abs pill pill-white" style="left:283px;top:13px;width:96px;height:17px">Book an Appointment</div>
  </div>

  <div class="abs photo" style="left:375px;top:342px;width:223px;height:205px;background:linear-gradient(180deg,#cfe9f5 0%,#a9cfe3 45%,#6f7f5a 75%,#3f3a2c 100%)" role="img" aria-label="Photo of a mother and daughter leaning on a wooden fence outdoors"></div>
  <h2 class="abs section-title" style="left:619px;top:393px">About <span>Me</span><i class="dot"></i></h2>
  <p class="abs body-small" style="left:619px;top:421px;width:188px;line-height:9px">Progressively fabricate enterprise-wide catalysts for change and high standards in testing procedures. Authoritatively re-engineer cooperative infrastructures for interdependent best practices. Objectively morph prospective content and turnkey mindshare. Dynamically embrace scalable communities whereas flexible solutions. Appropriately create superior e-commerce whereas bleeding-edge growth strategies.</p>
  <div class="abs pill pill-teal" style="left:619px;top:486px;width:63px;height:16px">Learn More</div>

  <section class="abs services">
    <h2>Our <b>Services</b></h2>
    <div class="svc" style="left:64px">
      <svg width="20" height="24" viewBox="0 0 20 24" fill="none" stroke="#fff" stroke-width="2"><circle cx="10" cy="4" r="3" fill="#fff"/><path d="M3 10h14M6 10v6h8v-6M7 16v6M13 16v6"/></svg>
      <h3>Child and Adolescent</h3>
      <p>Progressively fabricate wide catalysts<br>for change fabricate</p>
      <a>Learn More &rarr;</a>
    </div>
    <div class="svc" style="left:171px">
      <svg width="20" height="24" viewBox="0 0 20 24" fill="none" stroke="#fff" stroke-width="1.8"><path d="M5 9a5 6 0 0 1 10 0v3a5 6 0 0 1-10 0z"/><path d="M4 22c1-4 3-5 6-5s5 1 6 5"/></svg>
      <h3>Adult</h3>
      <p>Progressively fabricate wide catalysts<br>for change fabricate</p>
      <a>Learn More &rarr;</a>
    </div>
    <div class="svc" style="left:279px">
      <svg width="22" height="24" viewBox="0 0 22 24" fill="none" stroke="#fff" stroke-width="1.8"><circle cx="7" cy="3" r="2" fill="#fff"/><path d="M7 7v8h9l3 4M4 17h12"/><circle cx="6" cy="21" r="2"/><circle cx="15" cy="21" r="2"/></svg>
      <h3>Special Needs Parenting</h3>
      <p>Progressively fabricate wide catalysts<br>for change fabricate</p>
      <a>Learn More &rarr;</a>
    </div>
    <div class="svc" style="left:383px">
      <svg width="24" height="24" viewBox="0 0 24 24" fill="none" stroke="#fff" stroke-width="1.8"><path d="M8 4l4-2 4 2v5l-4 2-4-2z"/><path d="M2 8l4 8 3 6M22 8l-4 8-3 6"/></svg>
      <h3>Foster Care and Adoption</h3>
      <p>Progressively fabricate wide catalysts<br>for change fabricate</p>
      <a>Learn More &rarr;</a>
    </div>
  </section>

  <h2 class="abs section-title" style="left:375px;top:833px">Insurance</h2>
  <p class="abs body-small" style="left:375px;top:861px;width:188px;line-height:9px">Progressively fabricate enterprise-wide catalysts for change and high standards in testing procedures. Authoritatively re-engineer cooperative infrastructures for interdependent best practices. Objectively morph prospective content and turnkey mindshare. Dynamically embrace scalable communities whereas flexible solutions. Appropriately create superior e-commerce whereas bleeding-edge growth strategies.</p>
  <div class="abs pill pill-teal" style="left:375px;top:926px;width:63px;height:16px">Learn More</div>
  <div class="abs photo" style="left:600px;top:789px;width:222px;height:205px;background:linear-gradient(135deg,#3d4a26 0%,#6b7a35 40%,#a77a2c 75%,#d89a3a 100%)" role="img" aria-label="Photo of a smiling family with a young child outdoors in autumn"></div>

  <div class="abs band" style="left:376px;top:1019px;width:447px;height:43px">
    <span class="band-text" style="left:70px">Don't Wait to Get the Help You Need</span>
    <div class="abs pill pill-white" style="left:281px;top:13px;width:96px;height:17px">Book an Appointment</div>
  </div>

  <footer class="abs footer">
    <h4 style="left:35px">About Us</h4>
    <div class="col" style="left:35px;width:118px">Progressively fabricate enterprise-wide catalysts for change and high standards in testing procedures. Authoritatively re-engineer cooperative infrastructures for interdependent best practices.</div>
    <h4 style="left:204px">Quick Links</h4>
    <div class="col" style="left:204px">Home<br>About me<br>Insurnace<br>EMDR<br>Contact us</div>
    <h4 style="left:302px">Contact Details</h4>
    <div class="col" style="left:302px;line-height:normal">
      <div class="contact-row"><svg width="6" height="6" viewBox="0 0 10 10"><path d="M2 1l2 2-1 1.5a6 6 0 0 0 2.5 2.5L7 6l2 2-1.5 1.5C4 9 1 6 .5 2.5z" fill="#fff"/></svg>555 014 2231</div>
      <div class="contact-row"><svg width="6" height="5" viewBox="0 0 10 8"><rect width="10" height="8" fill="#fff"/><path d="M0 0l5 4 5-4" stroke="#2a2a2a" fill="none"/></svg>hello@brightmeadow.example</div>
      <div class="contact-row"><svg width="5" height="6" viewBox="0 0 8 10"><path d="M4 0a3 3 0 0 1 3 3c0 3-3 7-3 7S1 6 1 3a3 3 0 0 1 3-3z" fill="#fff"/></svg>48 Linden Lane, Riverton USA</div>
      <div class="socials"><span></span><span></span><span></span><span></span></div>
    </div>
  </footer>
  <div class="abs copy">&copy; Brightmeadow 2017-2018. All rights reserved.</div>

</div>
</body>
</html>
```